Business cards Marta Keller Sport & Events

I need new business cards to match my new logo design for my company called "Marta Keller Sport & Events". I'm based in Germany.
With my company, I offer different services in the context of sport.

Marta Keller owner

Marta Keller Sports & Events
Birkendorfer Weg 14
D-63158 Offenbach

+49 69 / 31 52 94 07
info@marta-keller-sport.example
www.marta-keller-sport.example

Contact Information for Business Card

Marta Keller Inhaberin Marta Keller Sport & Events Birkendorfer Weg 14 D-63158 Offenbach +49 69 / 31 52 94 07 info@marta-keller-sport.example www.marta-keller-sport.example

Requirements
Must have
• Logo | Double sided business card

```html
<!DOCTYPE html>
<html lang="de">
<head>
<meta charset="utf-8">
<title>Marta Keller Sport &amp; Events – Visitenkarten</title>
<link rel="stylesheet" href="https://fonts.googleapis.com/css2?family=Arimo:wght@400;700&display=swap">
<style>
  :root {
    --backdrop: #e6e6e4;
    --card-dark: #2a2a2c;
    --card-dark-edge: #222224;
    --card-light: #f4f4f3;
    --accent: #f39c1a;
    --text-dark: #2b2b2b;
    --text-light: #ffffff;
  }
  * { box-sizing: border-box; margin: 0; padding: 0; }
  html, body { width: 1200px; height: 801px; overflow: hidden; }
  body {
    background: var(--backdrop);
    font-family: "Arimo", Arial, sans-serif;
    position: relative;
  }
  .card {
    position: absolute;
    top: 225px;
    width: 540px;
    height: 350px;
    overflow: hidden;
    border-bottom: 3px solid var(--accent);
    box-shadow: 0 6px 18px rgba(0,0,0,0.18);
  }
  .card--front { left: 40px; background: var(--card-dark); }
  .card--back  { left: 620px; background: linear-gradient(135deg, var(--card-dark) 0%, var(--card-dark-edge) 100%); }
  .card__shape { position: absolute; inset: 0; }

  .wordmark {
    position: absolute;
    display: flex;
    align-items: center;
    gap: 12px;
    color: var(--text-light);
    font-weight: 700;
    letter-spacing: 1px;
    text-transform: uppercase;
  }
  .wordmark__dot {
    width: 46px; height: 46px;
    border-radius: 50%;
    background: var(--accent);
    flex: none;
  }
  .wordmark__name { font-size: 19px; line-height: 1.15; }
  .card--front .wordmark { left: 34px; top: 40px; }
  .card--back .wordmark { left: 120px; top: 150px; }

  .holder {
    position: absolute;
    left: 110px;
    top: 250px;
    width: 185px;
    text-align: right;
  }
  .holder__name {
    color: var(--accent);
    font-size: 12px;
    text-transform: uppercase;
    margin-bottom: 6px;
    white-space: nowrap;
  }
  .holder__line { color: var(--text-dark); font-size: 12px; line-height: 1.45; white-space: nowrap; }

  .divider {
    position: absolute;
    left: 308px; top: 246px;
    width: 1px; height: 66px;
    background: var(--text-dark);
  }

  .contact {
    position: absolute;
    left: 322px; top: 248px;
    list-style: none;
  }
  .contact__item {
    display: flex; align-items: center; gap: 7px;
    color: var(--text-dark);
    font-size: 11px;
    line-height: 20px;
    white-space: nowrap;
  }
  .contact__icon { width: 12px; height: 12px; flex: none; }
</style>
</head>
<body>

  <section class="card card--front" aria-label="Vorderseite">
    <svg class="card__shape" viewBox="0 0 540 350" aria-hidden="true">
      <path d="M540 10 C 530 110 420 150 300 165 C 170 182 80 210 50 350 L 540 350 Z" fill="#f4f4f3"/>
      <path d="M505 70 C 420 135 310 145 210 162 C 120 180 60 225 38 320 C 70 240 135 200 215 178 C 330 152 440 135 505 70 Z" fill="#f39c1a"/>
    </svg>

    <div class="wordmark">
      <span class="wordmark__dot"></span>
      <span class="wordmark__name">Marta Keller<br>Sport &amp; Events</span>
    </div>

    <div class="holder">
      <p class="holder__name">Marta Keller Inhaberin</p>
      <p class="holder__line">Birkendorfer Weg 14</p>
      <p class="holder__line">D-63158 Offenbach</p>
    </div>

    <span class="divider"></span>

    <ul class="contact">
      <li class="contact__item">
        <svg class="contact__icon" viewBox="0 0 12 12"><path d="M2.5 1 L4.5 1 L5.2 3.6 L3.9 4.6 C4.6 6 6 7.4 7.4 8.1 L8.4 6.8 L11 7.5 L11 9.5 C11 10.3 10.3 11 9.5 11 C5 11 1 7 1 2.5 C1 1.7 1.7 1 2.5 1 Z" fill="#f39c1a"/></svg>
        +49 69 / 31 52 94 07
      </li>
      <li class="contact__item">
        <svg class="contact__icon" viewBox="0 0 12 12"><rect x="0.5" y="2.5" width="11" height="7.5" fill="#f39c1a"/><path d="M0.5 2.5 L6 7 L11.5 2.5" fill="none" stroke="#fff" stroke-width="1"/></svg>
        info@marta-keller-sport.example
      </li>
      <li class="contact__item">
        <svg class="contact__icon" viewBox="0 0 12 12"><circle cx="6" cy="6" r="5.5" fill="#f39c1a"/><path d="M0.5 6 H11.5 M6 0.5 C3.5 3 3.5 9 6 11.5 M6 0.5 C8.5 3 8.5 9 6 11.5" fill="none" stroke="#fff" stroke-width="0.8"/></svg>
        www.marta-keller-sport.example
      </li>
    </ul>
  </section>

  <section class="card card--back" aria-label="Rückseite">
    <div class="wordmark">
      <span class="wordmark__dot"></span>
      <span class="wordmark__name">Marta Keller<br>Sport &amp; Events</span>
    </div>
  </section>

</body>
</html>
```